GLP letterhead

We need a letterhead design for our new company based in Los Angeles called "Gold Ladder Pictures". We develop film and television projects. We work with investors, financiers, film production companies, film distribution and sales companies as well as studios. We would like to incorporate our logo (see attached) but make the letterhead simple and elegant. We need to include: logo, company address, phone number and company website.
Updates

Hello designers, Thanks for your submissions. For our letterhead, we are looking for something more simple and elegant. No heavy bars or lines. Make it feel light and clean. Not a lot of ink on the page. Use the logo and contact info but think "clean", "streamlined" and mostly white paper. Looking forward to seeing more... thanks! Gold Ladder Pictures team

Target Market(s)

Studio executives, talent agents and agencies, financiers, investors.

Industry/Entity Type

It Company

Requirements
Must have
• Gold Ladder Pictures logo (see attached). Logo may be cropped and altered appropriately for elegant letterhead design.
• Please include:
• COMPANY ADDRESS:
• TQV Media Campus
• 2750 Halvering Avenue
• Norwick Center, 4th Floor
• Farrowdale Cove, CA 90999
• COMPANY WEBSITE:
• www.goldladderpicturesgroup.example
• COMPANY PHONE NUMBER:
• 555-014-2236

```html
<!DOCTYPE html>
<html lang="en">
<head>
<meta charset="utf-8">
<title>Gold Ladder Pictures – Stationery</title>
<link href="https://fonts.googleapis.com/css2?family=PT+Sans+Narrow:wght@400;700&display=swap" rel="stylesheet">
<style>
  :root {
    --backdrop: #e8e5e7;
    --ink: #000000;
    --paper: #ffffff;
    --accent: #1ba8de;
    --accent-soft: #8fd6f2;
    --text-dark: #3a3a3a;
    --text-light: #e9e9e9;
  }
  * { margin: 0; padding: 0; box-sizing: border-box; }
  html, body {
    width: 1200px; height: 1200px; overflow: hidden;
    background: var(--backdrop);
    font-family: "PT Sans Narrow", "Arial Narrow", sans-serif;
  }
  .canvas { position: relative; width: 1200px; height: 1200px; }

  .accent-stripe {
    position: absolute; left: 0; width: 100%; height: 8px;
    background: linear-gradient(90deg, var(--accent) 0%, var(--accent-soft) 25%, #ffffff 50%, var(--accent-soft) 75%, var(--accent) 100%);
  }

  /* Letterhead: light, mostly white paper */
  .letterhead {
    position: absolute; left: 66px; top: 97px; width: 711px; height: 1001px;
    background: var(--paper);
  }
  .letterhead__header {
    position: absolute; left: 0; top: 0; width: 100%; height: 150px;
  }
  .letterhead .accent-stripe {
    height: 2px;
    background: linear-gradient(90deg, var(--accent) 0%, var(--accent-soft) 35%, rgba(143,214,242,0) 50%, var(--accent-soft) 65%, var(--accent) 100%);
  }
  .letterhead__header .accent-stripe { top: 150px; left: 38px; width: calc(100% - 76px); }
  .letterhead__footer {
    position: absolute; left: 38px; bottom: 28px; width: calc(100% - 76px); height: 2px;
  }
  .letterhead__footer .accent-stripe { top: 0; width: 100%; }

  .address { font-size: 11px; line-height: 13px; color: var(--text-light); }
  .contact-list { list-style: none; font-size: 11px; line-height: 13px; color: var(--text-light); }
  .contact-list li { display: flex; align-items: center; gap: 5px; white-space: nowrap; }
  .contact-list svg { width: 8px; height: 8px; flex: none; }

  .letterhead .address { position: absolute; left: 38px; top: 43px; color: var(--text-dark); }
  .letterhead .contact-list { position: absolute; left: 38px; top: 109px; color: var(--text-dark); }

  .brand { position: absolute; display: flex; flex-direction: column; align-items: center; }
  .brand__dot { border-radius: 50%; background: var(--accent); }
  .brand__name {
    color: var(--accent); font-weight: 700; text-transform: uppercase;
    letter-spacing: 0.08em; white-space: nowrap;
  }
  .letterhead .brand { left: 504px; top: 26px; width: 160px; }
  .letterhead .brand__dot { width: 56px; height: 56px; }
  .letterhead .brand__name { margin-top: 18px; font-size: 14px; }

  /* Business cards */
  .card {
    position: absolute; left: 798px; width: 366px;
    background: var(--ink); border-radius: 6px; overflow: hidden;
  }
  .card--front { top: 166px; height: 214px; }
  .card--front .brand { left: 0; top: 44px; width: 100%; }
  .card--front .brand__dot { width: 72px; height: 72px; }
  .card--front .brand__name { margin-top: 24px; font-size: 17px; }

  .card--back { top: 407px; height: 223px; }
  .card--back .brand { left: 36px; top: 54px; width: 124px; }
  .card--back .brand__dot { width: 54px; height: 54px; }
  .card--back .brand__name { margin-top: 16px; font-size: 11.5px; }
  .card--back .accent-stripe { top: 201px; height: 10px; }
  .person { position: absolute; left: 206px; top: 34px; }
  .person__name { color: var(--accent); font-weight: 700; font-size: 14px; text-transform: uppercase; }
  .person__role { color: var(--text-light); font-size: 10px; margin-top: 1px; }
  .card--back .contact-list { position: absolute; left: 206px; top: 78px; font-size: 9px; line-height: 13px; }
  .card--back .address { position: absolute; left: 206px; top: 135px; font-size: 9px; line-height: 13px; }
</style>
</head>
<body>
<main class="canvas">

  <section class="letterhead" aria-label="Letterhead">
    <header class="letterhead__header">
      <p class="address">TQV Media Campus<br>2750 Halvering Avenue, Norwick Center,<br>4th Floor Farrowdale Cove, CA 90999</p>
      <ul class="contact-list">
        <li><svg viewBox="0 0 10 10"><path d="M2 0.5 L4 2.8 L3 4 Q4.3 6 6 7 L7.2 6 L9.5 8 L8 9.6 Q3.5 9 0.4 2 Z" fill="var(--accent)"/></svg>555-014-2236</li>
        <li><svg viewBox="0 0 10 10"><circle cx="5" cy="5" r="4.2" fill="none" stroke="var(--accent)" stroke-width="1.2"/><path d="M0.8 5 H9.2 M5 0.8 Q2.5 5 5 9.2 Q7.5 5 5 0.8" fill="none" stroke="var(--accent)" stroke-width="0.9"/></svg>www.goldladderpicturesgroup.example</li>
      </ul>
      <div class="brand">
        <span class="brand__dot"></span>
        <span class="brand__name">Gold Ladder Pictures</span>
      </div>
      <div class="accent-stripe"></div>
    </header>
    <footer class="letterhead__footer"><div class="accent-stripe"></div></footer>
  </section>

  <section class="card card--front" aria-label="Business card front">
    <div class="brand">
      <span class="brand__dot"></span>
      <span class="brand__name">Gold Ladder Pictures</span>
    </div>
  </section>

  <section class="card card--back" aria-label="Business card back">
    <div class="brand">
      <span class="brand__dot"></span>
      <span class="brand__name">Gold Ladder Pictures</span>
    </div>
    <div class="person">
      <p class="person__name">Marcus Ellery</p>
      <p class="person__role">Director</p>
    </div>
    <ul class="contact-list">
      <li><svg viewBox="0 0 10 10"><path d="M2 0.5 L4 2.8 L3 4 Q4.3 6 6 7 L7.2 6 L9.5 8 L8 9.6 Q3.5 9 0.4 2 Z" fill="var(--accent)"/></svg>555-014-2236</li>
      <li><svg viewBox="0 0 10 10"><rect x="0.5" y="2" width="9" height="6" fill="var(--accent)"/><path d="M0.5 2 L5 5.5 L9.5 2" fill="none" stroke="var(--ink)" stroke-width="0.8"/></svg>marcus@goldladderpicturesgroup.example</li>
      <li><svg viewBox="0 0 10 10"><circle cx="5" cy="5" r="4.2" fill="none" stroke="var(--accent)" stroke-width="1.2"/><path d="M0.8 5 H9.2 M5 0.8 Q2.5 5 5 9.2 Q7.5 5 5 0.8" fill="none" stroke="var(--accent)" stroke-width="0.9"/></svg>www.goldladderpicturesgroup.example</li>
    </ul>
    <p class="address">TQV Media Campus<br>2750 Halvering Avenue, Norwick Center,<br>4th Floor Farrowdale Cove, CA 90999</p>
    <div class="accent-stripe"></div>
  </section>

</main>
</body>
</html>
```